Ternic Business Card

I have a business that is called "Ternic Electrical Products LTD" My company deals with top of the range laptops and mobile phones that are exclusive. I need a business card that will be eye catching but not over complicated.

Target Market(s)

Adults aged 19 to 50
Upper middle class

Industry/Entity Type

Business

Requirements
Must have
• Company name/logo (file attached)
• It must have my contact information which is:

• Name: Dale Marwick

• Position: Managing Director 

• Business Address: 7 Hapton Row, London, W4 9QD

• Contact Number: 02085193604
• Mobile: 07814260537
• Email: info@ternic-goods.co.uk
Nice to have
• Simple and stylish
• Eye catching

```html
<!DOCTYPE html>
<html lang="en">
<head>
<meta charset="utf-8">
<title>Ternic Electrical Products – Business Card</title>
<link href="https://fonts.googleapis.com/css2?family=Questrial&family=Arimo:wght@400&display=swap" rel="stylesheet">
<style>
  :root {
    --page: #ffffff;
    --card-black: #000000;
    --card-charcoal: #333333;
    --brand-cyan: #3fd3ea;
    --brand-blue: #1f4f9c;
    --ink: #1a1a1a;
    --rule: #000000;
  }
  html, body {
    margin: 0;
    padding: 0;
    overflow: hidden;
  }
  body {
    width: 845px;
    height: 1200px;
    background: var(--page);
    position: relative;
  }
  .card {
    position: absolute;
    left: 239px;
    width: 342px;
    height: 220px;
    box-sizing: border-box;
    border: 1px solid var(--rule);
    overflow: hidden;
  }
  .card-front {
    display: flex;
    align-items: center;
    justify-content: center;
  }
  .card-front--black { background: var(--card-black); }
  .card-front--charcoal { background: var(--card-charcoal); }
  .card-back { background: var(--page); }

  .set-one .card-front { top: 78px; }
  .set-one .card-back { top: 317px; }
  .set-two .card-front { top: 655px; }
  .set-two .card-back { top: 898px; }

  .front-name {
    font-family: "Questrial", sans-serif;
    font-size: 40px;
    letter-spacing: 3px;
    color: var(--brand-cyan);
  }
  .brand-name {
    position: absolute;
    left: 8px;
    top: -4px;
    font-family: "Questrial", sans-serif;
    font-size: 86px;
    line-height: 86px;
    letter-spacing: 1px;
    color: var(--brand-cyan);
    white-space: nowrap;
  }
  .brand-tagline {
    position: absolute;
    left: 10px;
    top: 86px;
    font-family: "Questrial", sans-serif;
    font-size: 34px;
    line-height: 34px;
    letter-spacing: 0.5px;
    color: var(--brand-blue);
    white-space: nowrap;
  }
  .contact {
    position: absolute;
    top: 134px;
    margin: 0;
    font-family: "Arimo", sans-serif;
    font-size: 12px;
    line-height: 14.2px;
    color: var(--ink);
    font-style: normal;
    white-space: nowrap;
  }
  .contact-person { left: 11px; }
  .contact-details { left: 167px; }
</style>
</head>
<body>
  <section class="set-one">
    <div class="card card-front card-front--black">
      <span class="front-name">TERNIC</span>
    </div>
    <div class="card card-back">
      <div class="brand-name">TERNIC</div>
      <div class="brand-tagline">Electrical Products</div>
      <p class="contact contact-person">Dale Marwick<br>Managing Director</p>
      <address class="contact contact-details">7 Hapton Row<br>London<br>W4 9QD<br>02085193604<br>07814260537<br>info@ternic-goods.co.uk</address>
    </div>
  </section>

  <section class="set-two">
    <div class="card card-front card-front--charcoal">
      <span class="front-name">TERNIC</span>
    </div>
    <div class="card card-back">
      <div class="brand-name">TERNIC</div>
      <div class="brand-tagline">Electrical Products</div>
      <p class="contact contact-person">Dale Marwick<br>Managing Director</p>
      <address class="contact contact-details">7 Hapton Row<br>London<br>W4 9QD<br>02085193604<br>07814260537<br>info@ternic-goods.co.uk</address>
    </div>
  </section>
</body>
</html>
```